Popup Banners - BrightCounsel - Legal Technology

- We need two banners (same style) designed with two different images and different text.

- The details of the printing requirements are attached, along with suggested images.

- The banners should share the same theme as our website www.brightcounsel.com.au

- The first banner would include our logo (attached), use the 'roads join' image (attached) in some way and text: New Opportunities - Where legal services and technology meet.

- The second banner would include our logo (attached), use the 'jigsaw' image (attached) in some way and use text: Legal Technology Strategy, Advice and Capability.

- Details on what are required from the Printer is attached also.

Target Market(s)

Legal Professionals

Industry/Entity Type

Information Technology

Font styles to use
Sans Serif

Requirements
Must have
• Our logo (attached), suggested text and the image mentioned for each.
Nice to have
• Professional and modern look
Should not have
• Cheap looking

```html
<!DOCTYPE html>
<html lang="en">
<head>
<meta charset="utf-8">
<title>BrightCounsel – Popup Banners</title>
<link rel="stylesheet" href="https://fonts.googleapis.com/css2?family=Barlow+Semi+Condensed:wght@300;400&display=swap">
<style>
  :root {
    --page: #ffffff;
    --banner: #ffffff;
    --brand-blue: #57a0d3;
    --brand-charcoal: #5d5752;
    --fold-shade: #3e3a37;
    --ink: #5a5350;
    --ink-light: #ffffff;
  }
  * { margin: 0; padding: 0; box-sizing: border-box; }
  html, body {
    width: 1200px; height: 1200px; overflow: hidden;
    background: var(--page);
    font-family: "Barlow Semi Condensed", "Arial Narrow", sans-serif;
  }
  .banner {
    position: absolute; top: 102px;
    width: 402px; height: 993px;
    background: var(--banner);
    box-shadow: 0 6px 14px rgba(0,0,0,0.16), 0 0 3px rgba(0,0,0,0.08);
  }
  .banner--opportunities { left: 138px; }
  .banner--strategy { left: 696px; }
  .banner__art { position: absolute; inset: 0; }
  .brand {
    position: absolute; left: 26px; top: 30px;
    display: flex; align-items: center; gap: 12px;
    color: var(--ink); font-weight: 400; font-size: 23px; letter-spacing: 3px;
  }
  .brand__mark { width: 16px; height: 16px; background: var(--brand-blue); }
  .headline {
    position: absolute; left: 88px;
    color: var(--ink-light); font-weight: 400; font-size: 22px;
    letter-spacing: 0.6px; line-height: 38px; text-transform: uppercase;
  }
  .tagline {
    position: absolute; left: 88px;
    color: var(--ink); font-weight: 300; font-size: 22px;
    letter-spacing: 0.6px; line-height: 39px; text-transform: uppercase;
  }
  .banner--opportunities .headline { top: 338px; }
  .banner--opportunities .tagline { top: 454px; }
  .banner--strategy .headline { top: 318px; }
  .banner--strategy .tagline { top: 473px; }
</style>
</head>
<body>

<section class="banner banner--opportunities">
  <svg class="banner__art" viewBox="0 0 402 993" width="402" height="993">
    <defs>
      <linearGradient id="roads-tone" x1="0" y1="0" x2="0" y2="1">
        <stop offset="0" stop-color="#3f86c9"/>
        <stop offset="0.12" stop-color="#8ab8de"/>
        <stop offset="0.2" stop-color="#7a9a4a"/>
        <stop offset="0.6" stop-color="#5f8f32"/>
        <stop offset="1" stop-color="#3f6e24"/>
      </linearGradient>
    </defs>
    <g role="img" aria-label="Photo: two dirt roads joining on a green grassy hill under a blue sky">
      <polygon points="327,0 402,0 402,256 147,256" fill="url(#roads-tone)"/>
    </g>
    <polygon class="band band--blue" points="147,256 402,256 402,443 12,443" fill="var(--brand-blue)"/>
    <polygon class="band band--charcoal" points="94,290 402,290 402,408 12,408" fill="var(--brand-charcoal)"/>
    <polygon class="band__fold" points="12,408 36,408 28,419" fill="var(--fold-shade)"/>
  </svg>
  <div class="brand"><span class="brand__mark"></span>BrightCounsel</div>
  <p class="headline">New Opportunities -</p>
  <p class="tagline">Where legal services<br>and technology<br>come together</p>
</section>

<section class="banner banner--strategy">
  <svg class="banner__art" viewBox="0 0 402 993" width="402" height="993">
    <defs>
      <radialGradient id="jigsaw-tone" cx="0.62" cy="0.5" r="0.7">
        <stop offset="0" stop-color="#cfe6f6"/>
        <stop offset="0.3" stop-color="#5d94c4"/>
        <stop offset="0.7" stop-color="#234f7c"/>
        <stop offset="1" stop-color="#10294a"/>
      </radialGradient>
    </defs>
    <g role="img" aria-label="Photo: a hand placing a glowing jigsaw puzzle piece in blue light">
      <polygon points="327,0 402,0 402,256 147,256" fill="url(#jigsaw-tone)"/>
    </g>
    <polygon class="band band--blue" points="147,256 402,256 402,443 12,443" fill="var(--brand-blue)"/>
    <polygon class="band band--charcoal" points="94,290 402,290 402,408 12,408" fill="var(--brand-charcoal)"/>
    <polygon class="band__fold" points="12,408 36,408 28,419" fill="var(--fold-shade)"/>
  </svg>
  <div class="brand"><span class="brand__mark"></span>BrightCounsel</div>
  <p class="headline">Legal Technology<br>Strategy,</p>
  <p class="tagline">Advice and Capability</p>
</section>

</body>
</html>
```